Buchcover-Design für Ratgeber & Arbeitsbuch
Zielgruppe
Ratgeber und Arbeitsbuch, einfach geschrieben für Menschen, die mit Geld nicht gut umgehen können. Titel: Oje, das Konto ist schon leer. Soll Einsparpotenziale und Möglichkeiten der einfachen Geldanlage für jedermann darstellen. Liefert als Arbeitsbuch Checklisten und Tabellenblätter zum selbst ausfüllen.
Aufgabenstellung
Format A4 hoch, Zielgruppe junge Leute, die wenig Erfahrung im Umgang mit Geld haben. bei denen das Geld nie reicht und die bei der Selbstkontrolle Schwierigkeiten haben.

```html
<!DOCTYPE html>
<html lang="de">
<head>
<meta charset="utf-8">
<title>Oje, das Konto ist schon leer – Buchcover</title>
<link href="https://fonts.googleapis.com/css2?family=Raleway:wght@400;500;600&display=swap" rel="stylesheet">
<style>
  :root {
    --backdrop: #ede5ef;
    --cover-top: #4699e0;
    --cover-bottom: #5bb6f2;
    --spine: #1c4f82;
    --spine-dark: #123c66;
    --ink: #173f6b;
    --ink-soft: #1e4c7c;
    --pig-pink: #f2b8d2;
  }
  * { margin: 0; padding: 0; box-sizing: border-box; }
  html, body {
    width: 1200px;
    height: 1120px;
    overflow: hidden;
    background: var(--backdrop);
  }
  body { position: relative; font-family: "Raleway", sans-serif; }

  .book-cover {
    position: absolute;
    left: 249px;
    top: 60px;
    width: 702px;
    height: 1000px;
    background: linear-gradient(180deg, var(--cover-top) 0%, #4ea6e8 55%, var(--cover-bottom) 100%);
    box-shadow: 0 6px 18px rgba(60, 40, 80, 0.18);
    overflow: hidden;
  }
  .cover-spine {
    position: absolute;
    left: 0; top: 0;
    width: 64px; height: 100%;
    background: linear-gradient(180deg, var(--spine) 0%, var(--spine-dark) 100%);
  }
  .cover-author {
    position: absolute;
    left: 133px; top: 78px;
    font-size: 21px;
    font-weight: 500;
    letter-spacing: 0.5px;
    color: var(--ink-soft);
  }
  .cover-title {
    position: absolute;
    left: 133px; top: 212px;
    font-size: 51px;
    font-weight: 600;
    line-height: 1.06;
    color: var(--ink);
  }
  .cover-subtitle {
    position: absolute;
    left: 133px; top: 350px;
    font-size: 27px;
    font-weight: 500;
    color: var(--ink-soft);
  }
  .cover-illustration {
    position: absolute;
    left: 90px; top: 560px;
    width: 580px; height: 270px;
  }
  .cover-tagline {
    position: absolute;
    left: 113px; top: 868px;
    font-size: 17px;
    font-weight: 400;
    line-height: 1.42;
    color: var(--ink);
  }
</style>
</head>
<body>
  <div class="book-cover">
    <div class="cover-spine"></div>
    <p class="cover-author">DR. BERNHARD SOLM, HAMBURG</p>
    <h1 class="cover-title">Oje, das Konto<br>ist schon leer!</h1>
    <p class="cover-subtitle">Der Weg aus Deiner Finanznot</p>
    <svg class="cover-illustration" viewBox="0 0 580 270" role="img" aria-label="Foto: rosa Sparschweine, in wachsenden Stapeln von links nach rechts aufgereiht">
      <defs>
        <radialGradient id="pig-glow" cx="50%" cy="65%" r="60%">
          <stop offset="0%" stop-color="#f2b8d2" stop-opacity="0.55"/>
          <stop offset="100%" stop-color="#f2b8d2" stop-opacity="0"/>
        </radialGradient>
      </defs>
      <rect width="580" height="270" fill="url(#pig-glow)"/>
    </svg>
    <p class="cover-tagline">Ein Ratgeber und Arbeitsbuch für Leute,<br>die, trotz regelmäßigen Einkommens,<br>immer zu wenig Geld haben.</p>
  </div>
</body>
</html>
```